qZephyra - A forward thinking technology company in the greater Silicon Valley

A .ppt slide deck for a software consulting company. This slide deck will be used for project kick off meetings, sales proposals, and presentations to large audiences that report progress on a variety of projects. It should catch the eye with appealing creativity. Allow for flexibility in space and display. Project well both virtually and in person under varying light conditions. The finished product should give the impression that we are a custom shop but balance in appeal to larger, more traditional companies.

Review of the designs has been delayed due to holiday travel. Thank you for your submissions. I look forward to getting back to you the week of December 3rd.

Target Market(s)

We are an innovative technology company in the greater Silicon Valley. We design and build custom business analytics tools for large, retail corporations. Our solutions deal primarily in the supply chain space but we are leaning towards commercial construction and telecommunications industries. We are targeting prospective clients interested in machine learning and artificial intelligence. Our customers know quality and will pay for a custom solution that exceeds their expectations.

Industry/Entity Type

Business Software

Font styles to use
Sans Serif

Colors

Designer to choose colors to be used in the design.

Requirements
Must have
• Color, graphics, and photos. Multiple different template pages to appeal for graphs, pictures, text, or timelines.
Should not have
• Anything that resembles a "fidget spinner."

```html
<!DOCTYPE html>
<html lang="en">
<head>
<meta charset="utf-8">
<title>qZephyra – Presentation Template</title>
<link href="https://fonts.googleapis.com/css2?family=Montserrat:wght@300;400;600;700&display=swap" rel="stylesheet">
<style>
:root{
  --teal:#2b8a99;
  --teal-dark:#1d6472;
  --teal-light:#7cc3cc;
  --green:#84b13c;
  --green-dark:#5f8a2a;
  --blue:#2f5b93;
  --purple:#5a3f8f;
  --navy:#263746;
  --ink:#3c5566;
  --muted:#8d979e;
  --rule:#e2e6e9;
  --paper:#ffffff;
  --sky-1:#d8ecf4;
  --sky-2:#6fb0cf;
  --sky-3:#1f4e78;
}
*{box-sizing:border-box;margin:0;padding:0}
html,body{width:1200px;height:4354px;overflow:hidden;background:var(--paper)}
body{font-family:"Montserrat",Arial,sans-serif;color:var(--ink)}
.deck{display:grid;grid-template-columns:repeat(3,386px);grid-auto-rows:218px;gap:11px 12px;padding:7px 9px}
.slide{position:relative;overflow:hidden;background:var(--paper);border:1px solid var(--rule)}
.abs{position:absolute}
.title{position:absolute;left:14px;top:11px;font-size:10px;font-weight:600;letter-spacing:.3px;color:var(--ink);text-transform:uppercase}
.footer{position:absolute;left:14px;right:14px;bottom:6px;display:flex;justify-content:space-between;align-items:center;font-size:5px;color:var(--muted)}
.brand{display:inline-flex;align-items:center;gap:4px;font-weight:600;font-size:7px;color:var(--teal)}
.brand i{display:inline-block;width:6px;height:6px;background:currentColor}
.brand.light{color:#fff}
.brand.big{font-size:20px;gap:9px}
.brand.big i{width:15px;height:15px}
.photo{position:absolute}
.ph-sky{background:linear-gradient(135deg,var(--sky-1),var(--sky-2) 55%,var(--sky-3))}
.ph-teal{background:linear-gradient(135deg,#3d9aa8,#1d6472 60%,#113f4a)}
.ph-green{background:linear-gradient(135deg,#a9cc5b,#7ca63a 55%,#4d7424)}
.ph-dark{background:linear-gradient(135deg,#39424a,#1a2026)}
.ph-warm{background:linear-gradient(135deg,#e4d3bd,#b48c62 60%,#7a5a3c)}
.ph-city{background:linear-gradient(160deg,#eef4f8,#9cbfd8 50%,#3b6a93)}
.ph-grey{background:linear-gradient(135deg,#dfe4e8,#aab4bc)}
.tx{font-size:5px;line-height:1.55;color:var(--muted)}
.tx.w{color:#eaf4f6}
.head{font-size:8px;font-weight:700;color:var(--ink);text-transform:uppercase}
.head.w{color:#fff}
.bul{list-style:none}
.bul li{position:relative;padding-left:8px;font-size:5px;line-height:1.55;color:var(--muted);margin-bottom:4px}
.bul li::before{content:"";position:absolute;left:0;top:2px;width:3px;height:3px;background:var(--green)}
.box{position:absolute;padding:8px}
.bg-teal{background:var(--teal)}.bg-green{background:var(--green)}.bg-blue{background:var(--blue)}.bg-purple{background:var(--purple)}.bg-navy{background:var(--navy)}
.big-title{font-weight:300;color:#fff;text-transform:uppercase;line-height:1.15}
.agenda-row{display:flex;gap:10px;align-items:center;margin-bottom:7px;font-size:6px;color:var(--muted)}
.agenda-row b{font-size:12px;color:var(--teal);font-weight:700}
table.grid{border-collapse:collapse;position:absolute;font-size:5px;color:var(--muted)}
table.grid td,table.grid th{border-bottom:1px solid var(--rule);padding:2px 5px;text-align:left}
table.grid th{color:#fff;font-weight:600}
.member{position:absolute;top:62px;width:56px;text-align:center;font-size:5px;color:var(--muted)}
.member .avatar{width:42px;height:42px;margin:0 auto 6px;border-radius:50%}
.member b{display:block;font-size:6px;color:var(--ink);margin-bottom:2px}
.icon-label{position:absolute;width:60px;text-align:center;font-size:5px;color:var(--ink);font-weight:600}
svg{display:block}
</style>
</head>
<body>
<main class="deck">

<!-- 1 logo teal -->
<section class="slide ph-teal" role="img" aria-label="Opening slide with blue technology photograph">
  <div class="abs" style="left:0;right:0;top:96px;text-align:center"><span class="brand big light"><i></i>qZephyra</span></div>
</section>

<!-- 2 logo green -->
<section class="slide ph-green" role="img" aria-label="Opening slide with green technology photograph">
  <div class="abs" style="left:0;right:0;top:96px;text-align:center"><span class="brand big light"><i></i>qZephyra</span></div>
</section>

<!-- 3 title teal -->
<section class="slide ph-teal">
  <div class="photo" style="inset:0;background:linear-gradient(90deg,#12323c 0%,#1d6472 55%,#3d9aa8)" role="img" aria-label="Digital data network photograph"></div>
  <div class="abs" style="right:14px;top:10px"><span class="brand light"><i></i>qZephyra</span></div>
  <div class="abs" style="left:230px;top:70px">
    <div class="big-title" style="font-size:16px">Presentation<br>Title Here</div>
    <div style="font-size:7px;color:#d8eef1;margin-top:4px">Your Subtitle Here</div>
  </div>
</section>

<!-- 4 title green -->
<section class="slide">
  <div class="photo ph-green" style="inset:0" role="img" aria-label="Business desk photograph in green tone"></div>
  <div class="abs" style="left:14px;top:10px"><span class="brand light"><i></i>qZephyra</span></div>
  <div class="abs" style="left:14px;top:80px">
    <div class="big-title" style="font-size:16px">Presentation<br>Title Here.</div>
    <div style="font-size:7px;color:#eef6e0;margin-top:4px">Your Subtitle Here</div>
  </div>
</section>

<!-- 5 agenda -->
<section class="slide">
  <div class="photo" style="left:0;top:0;bottom:0;width:160px;background:linear-gradient(135deg,#9fd2d6,#3f9aa6)" role="img" aria-label="Person walking toward a bright window"></div>
  <div class="abs" style="left:200px;top:14px;font-size:11px;letter-spacing:1px;color:var(--ink)">AGENDA</div>
  <div class="abs" style="left:200px;top:40px">
    <div class="agenda-row"><b>01</b>Agenda Topic Here</div>
    <div class="agenda-row"><b>01</b>Agenda Topic Here</div>
    <div class="agenda-row"><b>01</b>Agenda Topic Here</div>
    <div class="agenda-row"><b>01</b>Agenda Topic Here</div>
    <div class="agenda-row"><b>01</b>Agenda Topic Here</div>
  </div>
  <div class="footer" style="left:174px"><span class="brand"><i></i>qZephyra</span><span>Presentation Title Here</span></div>
</section>

<!-- 6 text slide -->
<section class="slide">
  <div class="title">Text Slide</div>
  <div class="abs" style="left:14px;right:14px;top:32px">
    <p class="tx">Share key project insights and progress with your team here. Describe scope, goals, timing and the people involved in delivery. Keep every paragraph short so the room can follow along with ease and clarity.</p><br>
    <p class="tx">Share key project insights and progress with your team here. Describe scope, goals, timing and the people involved in delivery. Keep every paragraph short so the room can follow along with ease and clarity.</p><br>
    <p class="tx">Share key project insights and progress with your team here. Describe scope, goals, timing and the people involved in delivery. Keep every paragraph short so the room can follow along with ease and clarity.</p><br>
    <p class="tx">Share key project insights and progress with your team here. Describe scope, goals, timing and the people involved in delivery.</p>
  </div>
  <div class="footer"><span class="brand"><i></i>qZephyra</span><span>Presentation Title Here</span></div>
</section>

<!-- 7 bullets -->
<section class="slide">
  <div class="title">Bullets Slide</div>
  <ul class="bul abs" style="left:14px;right:14px;top:34px">
    <li>Share key project insights and progress with your team here. Describe scope, goals, timing and the people involved in delivery.</li>
    <li>Share key project insights and progress with your team here. Describe scope, goals, timing and the people involved in delivery.</li>
    <li>Share key project insights and progress with your team here. Describe scope, goals, timing and the people involved in delivery.</li>
    <li>Share key project insights and progress with your team here. Describe scope, goals, timing and the people involved in delivery.</li>
  </ul>
  <div class="footer"><span class="brand"><i></i>qZephyra</span><span>Presentation Title Here</span></div>
</section>

<!-- 8 bullets level 1 -->
<section class="slide">
  <div class="title">Bullets Slide Level 1</div>
  <ul class="bul abs" style="left:14px;right:14px;top:34px">
    <li>Share key project insights and progress with your team here.</li>
    <li style="margin-left:10px">Describe scope, goals, timing and the people involved.</li>
    <li>Share key project insights and progress with your team here.</li>
    <li style="margin-left:10px">Describe scope, goals, timing and the people involved.</li>
    <li>Share key project insights and progress with your team here.</li>
    <li style="margin-left:10px">Describe scope, goals, timing and the people involved.</li>
  </ul>
  <div class="footer"><span class="brand"><i></i>qZephyra</span><span>Presentation Title Here</span></div>
</section>

<!-- 9 bullets and image -->
<section class="slide">
  <div class="title">Bullets and Image</div>
  <ul class="bul abs" style="left:14px;width:170px;top:34px">
    <li>Share key project insights and progress with your team here.</li>
    <li>Describe scope, goals, timing and the people involved.</li>
    <li>Share key project insights and progress with your team here.</li>
    <li>Describe scope, goals, timing and the people involved.</li>
    <li>Share key project insights and progress with your team here.</li>
  </ul>
  <div class="photo ph-city" style="left:200px;right:14px;top:34px;height:140px" role="img" aria-label="Glass office towers seen from below"></div>
  <div class="footer"><span class="brand"><i></i>qZephyra</span><span>Presentation Title Here</span></div>
</section>

<!-- 10 two column bullets -->
<section class="slide">
  <div class="title">Two Column Bullets Slide</div>
  <ul class="bul abs" style="left:14px;width:170px;top:34px">
    <li><b style="color:var(--ink)">Your Heading Here</b><br>Describe scope, goals and timing.</li>
    <li><b style="color:var(--ink)">Your Heading Here</b><br>Describe scope, goals and timing.</li>
    <li><b style="color:var(--ink)">Your Heading Here</b><br>Describe scope, goals and timing.</li>
    <li><b style="color:var(--ink)">Your Heading Here</b><br>Describe scope, goals and timing.</li>
  </ul>
  <ul class="bul abs" style="left:200px;width:170px;top:34px">
    <li><b style="color:var(--ink)">Your Heading Here</b><br>Describe scope, goals and timing.</li>
    <li><b style="color:var(--ink)">Your Heading Here</b><br>Describe scope, goals and timing.</li>
    <li><b style="color:var(--ink)">Your Heading Here</b><br>Describe scope, goals and timing.</li>
    <li><b style="color:var(--ink)">Your Heading Here</b><br>Describe scope, goals and timing.</li>
  </ul>
  <div class="footer"><span class="brand"><i></i>qZephyra</span><span>Presentation Title Here</span></div>
</section>

<!-- 11 image slide -->
<section class="slide">
  <div class="title">Image Slide</div>
  <div class="photo ph-city" style="left:100px;right:0;top:32px;height:110px" role="img" aria-label="Businessman overlooking a city skyline"></div>
  <div class="box bg-purple" style="left:14px;top:42px;width:120px;height:60px">
    <div class="head w" style="font-size:7px">We are here for you</div>
    <p class="tx w" style="margin-top:3px">Our approach to the tasks and solutions for your business.</p>
  </div>
  <svg class="abs" style="left:40px;top:150px" width="40" height="30" viewBox="0 0 40 30"><circle cx="20" cy="15" r="12" fill="none" stroke="var(--teal)" stroke-width="2"/><path d="M14 15l4 4 8-8" fill="none" stroke="var(--teal)" stroke-width="2"/></svg>
  <div class="footer"><span class="brand"><i></i>qZephyra</span><span>Presentation Title Here</span></div>
</section>

<!-- 12 portfolio -->
<section class="slide">
  <div class="title">Portfolio</div>
  <div class="photo ph-teal" style="left:14px;top:30px;width:76px;height:72px" role="img" aria-label="Team meeting photograph"></div>
  <div class="box bg-teal" style="left:94px;top:30px;width:90px;height:72px"><div class="head w" style="font-size:6px">Portfolio Name</div><p class="tx w">Short project summary line.</p></div>
  <div class="box bg-green" style="left:190px;top:30px;width:90px;height:72px"><div class="head w" style="font-size:6px">Portfolio Name</div><p class="tx w">Short project summary line.</p></div>
  <div class="photo ph-warm" style="left:286px;top:30px;width:86px;height:72px" role="img" aria-label="Sunlit landscape photograph"></div>
  <div class="photo ph-city" style="left:14px;top:106px;width:76px;height:72px" role="img" aria-label="People silhouetted against windows"></div>
  <div class="photo ph-sky" style="left:94px;top:106px;width:90px;height:72px" role="img" aria-label="Office tower photograph"></div>
  <div class="box bg-blue" style="left:190px;top:106px;width:90px;height:72px"><div class="head w" style="font-size:6px">Portfolio Name</div><p class="tx w">Short project summary line.</p></div>
  <div class="photo ph-grey" style="left:286px;top:106px;width:86px;height:72px" role="img" aria-label="Workspace photograph"></div>
  <div class="footer"><span class="brand"><i></i>qZephyra</span><span>Presentation Title Here</span></div>
</section>

<!-- 13 divider blue -->
<section class="slide">
  <div class="photo" style="inset:0;background:linear-gradient(135deg,#b8dbe8,#4f93b8 50%,#1d4b72)" role="img" aria-label="Glass skyscraper photograph"></div>
  <div class="abs" style="left:14px;top:100px"><div class="big-title" style="font-size:15px">This is your divider page</div><div style="font-size:6px;color:#e0eef4;margin-top:3px">Your Subtitle Here</div></div>
</section>

<!-- 14 table -->
<section class="slide">
  <div class="title">Your Table Slide</div>
  <table class="grid" style="left:40px;top:32px;width:306px">
    <tr><th style="background:var(--teal)">Item</th><th style="background:var(--teal)">2016</th><th style="background:var(--purple)">2017</th><th style="background:var(--teal)">2018</th></tr>
    <tr><td>Table Item Here</td><td>20</td><td style="background:var(--purple);color:#fff">35</td><td>40</td></tr>
    <tr><td>Table Item Here</td><td>18</td><td style="background:var(--green);color:#fff">32</td><td>38</td></tr>
    <tr><td>Table Item Here</td><td>22</td><td style="background:var(--purple);color:#fff">30</td><td>41</td></tr>
    <tr><td>Table Item Here</td><td>15</td><td style="background:var(--blue);color:#fff">28</td><td>36</td></tr>
    <tr><td>Table Item Here</td><td>19</td><td>26</td><td>33</td></tr>
    <tr><td>Table Item Here</td><td>24</td><td>31</td><td>39</td></tr>
    <tr><td>Table Item Here</td><td>21</td><td>27</td><td>35</td></tr>
  </table>
  <div class="footer"><span class="brand"><i></i>qZephyra</span><span>Presentation Title Here</span></div>
</section>

<!-- 15 we always here teal -->
<section class="slide bg-teal">
  <div class="photo" style="left:14px;top:60px;width:150px;height:100px;background:linear-gradient(135deg,#b9dfe3,#5aa7b2)" role="img" aria-label="Team collaborating at a table"></div>
  <div class="abs" style="left:190px;top:50px;width:170px"><div style="font-size:13px;font-weight:300;color:#fff;text-transform:uppercase">We always here</div><p class="tx w" style="margin-top:6px;font-size:6px">Our short and precise slogan describes our approach to the tasks and solutions, and it is a summary of those.</p></div>
  <div class="abs" style="left:30px;top:100px;font-size:7px;color:#fff;font-weight:600">WE ARE HERE FOR YOU</div>
</section>

<!-- 16 we always here photo -->
<section class="slide">
  <div class="photo ph-sky" style="left:0;top:0;bottom:26px;width:190px" role="img" aria-label="Skyscraper facade photograph"></div>
  <div class="box bg-navy" style="left:190px;top:0;right:0;bottom:26px;padding:20px 16px">
    <div style="font-size:12px;font-weight:300;color:#fff;text-transform:uppercase">We always here</div>
    <p class="tx w" style="margin-top:6px;font-size:6px">Our short and precise slogan describes our approach to the tasks and solutions, and it is a summary of those.</p>
  </div>
  <div class="footer"><span class="brand"><i></i>qZephyra</span><span>Presentation Title Here</span></div>
</section>

<!-- 17 our team circles -->
<section class="slide">
  <div class="title" style="left:0;right:0;text-align:center">Our Team</div>
  <div class="member" style="left:24px"><div class="avatar ph-grey" role="img" aria-label="Team member portrait"></div><b>Team Member</b>Job Title</div>
  <div class="member" style="left:92px"><div class="avatar ph-grey" role="img" aria-label="Team member portrait"></div><b>Team Member</b>Job Title</div>
  <div class="member" style="left:160px"><div class="avatar ph-grey" role="img" aria-label="Team member portrait"></div><b>Team Member</b>Job Title</div>
  <div class="member" style="left:228px"><div class="avatar ph-grey" role="img" aria-label="Team member portrait"></div><b>Team Member</b>Job Title</div>
  <div class="member" style="left:296px"><div class="avatar ph-grey" role="img" aria-label="Team member portrait"></div><b>Team Member</b>Job Title</div>
  <div class="footer"><span class="brand"><i></i>qZephyra</span><span>Presentation Title Here</span></div>
</section>

<!-- 18 our team squares -->
<section class="slide">
  <div class="title">Our Team</div>
  <div class="member" style="left:18px;top:52px"><div class="avatar ph-grey" style="border-radius:0" role="img" aria-label="Team member portrait"></div><b>Team Member</b>Job Title</div>
  <div class="member" style="left:88px;top:52px"><div class="avatar ph-grey" style="border-radius:0" role="img" aria-label="Team member portrait"></div><b>Team Member</b>Job Title</div>
  <div class="member" style="left:158px;top:52px"><div class="avatar ph-grey" style="border-radius:0" role="img" aria-label="Team member portrait"></div><b>Team Member</b>Job Title</div>
  <div class="member" style="left:228px;top:52px"><div class="avatar ph-grey" style="border-radius:0" role="img" aria-label="Team member portrait"></div><b>Team Member</b>Job Title</div>
  <div class="member" style="left:298px;top:52px"><div class="avatar ph-grey" style="border-radius:0" role="img" aria-label="Team member portrait"></div><b>Team Member</b>Job Title</div>
  <div class="abs bg-teal" style="left:14px;right:14px;top:150px;height:3px"></div>
  <div class="footer"><span class="brand"><i></i>qZephyra</span><span>Presentation Title Here</span></div>
</section>

<!-- 19 divider green -->
<section class="slide">
  <div class="photo ph-green" style="inset:0" role="img" aria-label="City skyline in green tone"></div>
  <div class="abs" style="left:0;right:0;top:78px;text-align:center"><span class="brand light" style="font-size:11px"><i></i>qZephyra</span><div class="big-title" style="font-size:14px;margin-top:8px">This is your divider page</div><div style="font-size:6px;color:#eef6e0;margin-top:3px">Your Subtitle Here</div></div>
</section>

<!-- 20 mockup -->
<section class="slide">
  <div class="title">Our Mock Up</div>
  <div class="photo" style="left:30px;top:40px;width:170px;height:130px;background:linear-gradient(135deg,#e8edf1,#9fb2c1)" role="img" aria-label="Desktop computer and laptop showing a website"></div>
  <div class="abs" style="left:230px;top:50px">
    <div class="agenda-row"><svg width="12" height="12"><circle cx="6" cy="6" r="6" fill="var(--teal)"/></svg><span><b style="font-size:6px;color:var(--ink)">Heading Here</b><br>Short description.</span></div>
    <div class="agenda-row"><svg width="12" height="12"><circle cx="6" cy="6" r="6" fill="var(--green)"/></svg><span><b style="font-size:6px;color:var(--ink)">Heading Here</b><br>Short description.</span></div>
    <div class="agenda-row"><svg width="12" height="12"><circle cx="6" cy="6" r="6" fill="var(--blue)"/></svg><span><b style="font-size:6px;color:var(--ink)">Heading Here</b><br>Short description.</span></div>
    <div class="agenda-row"><svg width="12" height="12"><circle cx="6" cy="6" r="6" fill="var(--purple)"/></svg><span><b style="font-size:6px;color:var(--ink)">Heading Here</b><br>Short description.</span></div>
  </div>
  <div class="footer"><span class="brand"><i></i>qZephyra</span><span>Presentation Title Here</span></div>
</section>

<!-- 21 portfolio showcase -->
<section class="slide">
  <div class="title">Portfolio Showcase</div>
  <div class="photo ph-warm" style="left:14px;top:30px;width:110px;height:70px" role="img" aria-label="Hands on a desk photograph"></div>
  <div class="box bg-teal" style="left:128px;top:30px;width:90px;height:70px"><div class="head w" style="font-size:6px">Heading Goes Here</div></div>
  <div class="photo ph-sky" style="left:222px;top:30px;width:150px;height:70px" role="img" aria-label="Modern office photograph"></div>
  <div class="box bg-teal" style="left:14px;top:104px;width:110px;height:70px"><div class="head w" style="font-size:6px">Heading Goes Here</div></div>
  <div class="photo ph-city" style="left:128px;top:104px;width:130px;height:70px" role="img" aria-label="Laptop workspace photograph"></div>
  <div class="box bg-green" style="left:262px;top:104px;width:110px;height:70px"><div class="head w" style="font-size:6px">Heading Goes Here</div></div>
  <div class="footer"><span class="brand"><i></i>qZephyra</span><span>Presentation Title Here</span></div>
</section>

<!-- 22 bullet & chart pie -->
<section class="slide">
  <div class="title">Bullet &amp; Chart Area</div>
  <svg class="abs" style="left:30px;top:40px" width="130" height="130" viewBox="0 0 130 130">
    <g transform="rotate(-90 65 65)">
      <circle cx="65" cy="65" r="30" fill="none" stroke="var(--teal)" stroke-width="60" stroke-dasharray="94.2 188.5"/>
      <circle cx="65" cy="65" r="30" fill="none" stroke="var(--green)" stroke-width="60" stroke-dasharray="47.1 188.5" stroke-dashoffset="-94.2"/>
      <circle cx="65" cy="65" r="30" fill="none" stroke="var(--purple)" stroke-width="60" stroke-dasharray="28.3 188.5" stroke-dashoffset="-141.3"/>
      <circle cx="65" cy="65" r="30" fill="none" stroke="var(--blue)" stroke-width="60" stroke-dasharray="18.9 188.5" stroke-dashoffset="-169.6"/>
    </g>
    <text x="122" y="70" font-size="9" fill="var(--ink)" text-anchor="end">50%</text>
    <text x="8" y="90" font-size="9" fill="var(--ink)">25%</text>
    <text x="4" y="48" font-size="9" fill="var(--ink)">15%</text>
    <text x="40" y="12" font-size="9" fill="var(--ink)">10%</text>
  </svg>
  <ul class="bul abs" style="left:200px;top:50px;width:170px">
    <li>Category One – describe data here.</li>
    <li>Category Two – describe data here.</li>
    <li>Category Three – describe data here.</li>
    <li>Category Four – describe data here.</li>
  </ul>
  <div class="footer"><span class="brand"><i></i>qZephyra</span><span>Presentation Title Here</span></div>
</section>

<!-- 23 bullet & chart bars -->
<section class="slide">
  <div class="title">Bullet &amp; Chart Area</div>
  <div class="abs" style="left:14px;top:36px;font-size:14px;line-height:1.15;color:var(--teal);font-weight:300">60<br><span style="color:var(--green)">30</span><br><span style="color:var(--blue)">50</span><br><span style="color:var(--purple)">%</span></div>
  <ul class="bul abs" style="left:46px;top:40px;width:110px"><li>Your Title Here</li><li>Your Title Here</li><li>Your Title Here</li><li>Your Title Here</li></ul>
  <svg class="abs" style="left:180px;top:40px" width="190" height="130" viewBox="0 0 190 130">
    <line x1="0" y1="125" x2="190" y2="125" stroke="var(--rule)"/>
    <g fill="var(--teal)"><rect x="10" y="70" width="8" height="55"/><rect x="55" y="40" width="8" height="85"/><rect x="100" y="60" width="8" height="65"/><rect x="145" y="30" width="8" height="95"/></g>
    <g fill="var(--green)"><rect x="20" y="55" width="8" height="70"/><rect x="65" y="80" width="8" height="45"/><rect x="110" y="35" width="8" height="90"/><rect x="155" y="65" width="8" height="60"/></g>
    <g fill="var(--purple)"><rect x="30" y="90" width="8" height="35"/><rect x="75" y="60" width="8" height="65"/><rect x="120" y="85" width="8" height="40"/><rect x="165" y="50" width="8" height="75"/></g>
  </svg>
  <div class="footer"><span class="brand"><i></i>qZephyra</span><span>Presentation Title Here</span></div>
</section>

<!-- 24 image + icons -->
<section class="slide">
  <div class="title">Image + Icons</div>
  <div class="photo ph-warm" style="left:0;right:0;top:28px;height:80px;background:linear-gradient(90deg,#c9b79d,#8da6ba,#b7c6d2)" role="img" aria-label="Bright office lobby photograph"></div>
  <svg class="abs" style="left:0;top:86px" width="386" height="50" viewBox="0 0 386 50">
    <g fill="var(--teal)" stroke="#fff" stroke-width="3"><circle cx="60" cy="22" r="20"/><circle cx="150" cy="22" r="20"/><circle cx="240" cy="22" r="20"/><circle cx="330" cy="22" r="20"/></g>
    <g fill="none" stroke="#fff" stroke-width="1.5"><rect x="53" y="16" width="14" height="11"/><circle cx="150" cy="22" r="6"/><path d="M233 28l7-12 7 12z"/><path d="M324 22h12M330 16v12"/></g>
  </svg>
  <div class="icon-label" style="left:30px;top:140px">Heading Goes Here</div>
  <div class="icon-label" style="left:120px;top:140px">Heading Goes Here</div>
  <div class="icon-label" style="left:210px;top:140px">Heading Goes Here</div>
  <div class="icon-label" style="left:300px;top:140px">Heading Goes Here</div>
  <div class="footer"><span class="brand"><i></i>qZephyra</span><span>Presentation Title Here</span></div>
</section>

<!-- 25 image + icons teal -->
<section class="slide">
  <div class="title">Image + Icons</div>
  <div class="photo ph-sky" style="left:0;right:0;top:28px;height:60px" role="img" aria-label="Aerial city photograph"></div>
  <div class="box bg-teal" style="left:110px;top:40px;width:120px;height:60px"><div class="head w" style="font-size:6px">Heading Goes Here</div><p class="tx w">Short description line.</p></div>
  <svg class="abs" style="left:0;top:110px" width="386" height="30" viewBox="0 0 386 30"><g fill="none" stroke="var(--teal)" stroke-width="1.5"><circle cx="50" cy="15" r="12"/><circle cx="140" cy="15" r="12"/><circle cx="230" cy="15" r="12"/><circle cx="320" cy="15" r="12"/></g></svg>
  <div class="icon-label" style="left:20px;top:146px">Heading Goes Here</div>
  <div class="icon-label" style="left:110px;top:146px">Heading Goes Here</div>
  <div class="icon-label" style="left:200px;top:146px">Heading Goes Here</div>
  <div class="icon-label" style="left:290px;top:146px">Heading Goes Here</div>
  <div class="footer"><span class="brand"><i></i>qZephyra</span><span>Presentation Title Here</span></div>
</section>

<!-- 26 image + bullets + text -->
<section class="slide">
  <div class="title">Image + Bullets + Text</div>
  <div class="abs" style="left:14px;top:36px;width:160px">
    <div class="agenda-row"><svg width="16" height="16"><circle cx="8" cy="8" r="8" fill="var(--teal)"/></svg><span><b style="font-size:6px;color:var(--ink)">Heading Goes Here</b><br>Short description line.</span></div>
    <div class="agenda-row"><svg width="16" height="16"><circle cx="8" cy="8" r="8" fill="var(--teal)"/></svg><span><b style="font-size:6px;color:var(--ink)">Heading Goes Here</b><br>Short description line.</span></div>
    <div class="agenda-row"><svg width="16" height="16"><circle cx="8" cy="8" r="8" fill="var(--teal)"/></svg><span><b style="font-size:6px;color:var(--ink)">Heading Goes Here</b><br>Short description line.</span></div>
  </div>
  <div class="photo ph-sky" style="left:190px;right:14px;top:30px;height:110px" role="img" aria-label="Businessman in front of bright sky"></div>
  <div class="box bg-teal" style="left:14px;top:140px;width:200px;height:40px"><p class="tx w">Share key project insights and progress with your team here.</p></div>
  <div class="footer"><span class="brand"><i></i>qZephyra</span><span>Presentation Title Here</span></div>
</section>

<!-- 27 text slide dark -->
<section class="slide">
  <div class="title">Text Slide</div>
  <div class="photo ph-dark" style="left:0;right:0;top:28px;bottom:26px" role="img" aria-label="Dark city photograph"></div>
  <div class="abs" style="left:14px;top:40px;width:170px"><div class="head w" style="font-size:10px">Heading Here</div><p class="tx w" style="margin-top:4px">Share key project insights and progress with your team here. Describe scope, goals, timing and the people involved in delivery. Keep every paragraph short so the room can follow along.</p></div>
  <div class="abs" style="left:200px;top:40px;width:170px"><div class="head w" style="font-size:10px">Heading Here</div><p class="tx w" style="margin-top:4px">Share key project insights and progress with your team here. Describe scope, goals, timing and the people involved in delivery. Keep every paragraph short so the room can follow along.</p></div>
  <div class="footer"><span class="brand"><i></i>qZephyra</span><span>Presentation Title Here</span></div>
</section>

<!-- 28 blank -->
<section class="slide">
  <div class="title">Your Blank Slide</div>
  <div class="footer"><span class="brand"><i></i>qZephyra</span><span>Presentation Title Here</span></div>
</section>

<!-- 29 images + text -->
<section class="slide">
  <div class="title">Images + Text</div>
  <div class="box bg-teal" style="left:14px;top:30px;width:160px;height:60px"><div class="head w">Heading Here</div><p class="tx w">Share key project insights with your team.</p></div>
  <div class="box bg-green" style="left:270px;top:30px;width:100px;height:60px"><p class="tx w">Short note about the result.</p></div>
  <div class="photo ph-sky" style="left:14px;top:96px;width:175px;height:80px" role="img" aria-label="Light rays through glass roof"></div>
  <div class="photo ph-warm" style="left:195px;top:96px;width:175px;height:80px" role="img" aria-label="Sunset over city photograph"></div>
  <div class="footer"><span class="brand"><i></i>qZephyra</span><span>Presentation Title Here</span></div>
</section>

<!-- 30 images + bullets -->
<section class="slide">
  <div class="title">Images + Bullets</div>
  <div class="photo ph-sky" style="left:14px;top:30px;width:170px;height:150px" role="img" aria-label="Bright glass architecture photograph"></div>
  <div class="abs" style="left:200px;top:40px">
    <div class="agenda-row"><svg width="12" height="12"><rect width="12" height="12" fill="none" stroke="var(--teal)"/></svg>Heading Here</div>
    <div class="agenda-row"><svg width="12" height="12"><rect width="12" height="12" fill="none" stroke="var(--teal)"/></svg>Heading Here</div>
    <div class="agenda-row"><svg width="12" height="12"><rect width="12" height="12" fill="none" stroke="var(--teal)"/></svg>Heading Here</div>
    <div class="agenda-row"><svg width="12" height="12"><rect width="12" height="12" fill="none" stroke="var(--teal)"/></svg>Heading Here</div>
    <div class="agenda-row"><svg width="12" height="12"><rect width="12" height="12" fill="none" stroke="var(--teal)"/></svg>Heading Here</div>
  </div>
  <div class="footer"><span class="brand"><i></i>qZephyra</span><span>Presentation Title Here</span></div>
</section>

<!-- 31 image + text -->
<section class="slide">
  <div class="title">Image + Text</div>
  <div class="photo ph-warm" style="left:150px;right:0;top:28px;bottom:26px" role="img" aria-label="Wooden blocks stacked on a table"></div>
  <div class="box bg-teal" style="left:14px;top:40px;width:160px;height:120px"><div class="head w" style="font-size:10px">Heading Here</div><p class="tx w" style="margin-top:4px">Share key project insights and progress with your team here. Describe scope, goals, timing and the people involved.</p></div>
  <div class="footer"><span class="brand"><i></i>qZephyra</span><span>Presentation Title Here</span></div>
</section>

<!-- 32 images + text -->
<section class="slide">
  <div class="title">Images + Text</div>
  <div class="photo ph-city" style="left:14px;top:34px;width:110px;height:70px" role="img" aria-label="Waterfront city photograph"></div>
  <div class="photo ph-warm" style="left:200px;top:30px;right:14px;height:150px;background:linear-gradient(135deg,#fff3d9,#8cb4cf 60%,#2e5d84)" role="img" aria-label="Sunburst over skyscrapers"></div>
  <div class="box bg-teal" style="left:130px;top:70px;width:110px;height:80px"><p class="tx w">Share key project insights and progress with your team here.</p></div>
  <p class="tx abs" style="left:14px;top:112px;width:110px">Describe scope, goals, timing and the people involved.</p>
  <div class="footer"><span class="brand"><i></i>qZephyra</span><span>Presentation Title Here</span></div>
</section>

<!-- 33 timeline logo -->
<section class="slide">
  <div class="title">Our Time Line</div>
  <div class="abs" style="left:150px;top:30px"><span class="brand" style="font-size:9px"><i></i>qZephyra</span></div>
  <div class="abs" style="left:193px;top:46px;width:1px;height:150px;background:var(--rule)"></div>
  <div class="abs tx" style="left:200px;top:70px"><b style="color:var(--ink)">Milestone</b><br>Short note here.</div>
  <div class="abs tx" style="left:130px;top:110px;text-align:right"><b style="color:var(--ink)">Milestone</b><br>Short note here.</div>
  <div class="abs tx" style="left:200px;top:150px"><b style="color:var(--ink)">Milestone</b><br>Short note here.</div>
</section>

<!-- 34 heading photo -->
<section class="slide">
  <div class="photo" style="inset:0;background:linear-gradient(135deg,#6f8c99,#2f4a56)" role="img" aria-label="Team hands joined over a table seen from above"></div>
  <div class="abs" style="left:14px;top:70px;width:180px"><div class="head w" style="font-size:10px">Heading Here</div><p class="tx w" style="margin-top:4px">Share key project insights and progress with your team here. Describe scope, goals, timing and the people involved in delivery.</p></div>
</section>

<!-- 35 editable icons -->
<section class="slide">
  <div class="title">Editable Icons</div>
  <svg class="abs" style="left:20px;top:36px" width="346" height="140" viewBox="0 0 346 140">
    <g fill="none" stroke="var(--teal)" stroke-width="1.6">
      <circle cx="10" cy="10" r="7"/><rect x="30" y="3" width="14" height="14"/><path d="M64 17l7-14 7 14z"/><path d="M96 10h14M103 3v14"/><circle cx="130" cy="10" r="7"/><path d="M150 3h14v14h-14z"/><path d="M182 10l7-7 7 7-7 7z"/><circle cx="220" cy="10" r="7"/><path d="M240 17l7-14 7 14z"/><rect x="272" y="3" width="14" height="14"/><circle cx="310" cy="10" r="7"/><path d="M326 10h14M333 3v14"/>
      <rect x="3" y="33" width="14" height="14"/><circle cx="37" cy="40" r="7"/><path d="M63 40h14M70 33v14"/><path d="M96 47l7-14 7 14z"/><rect x="123" y="33" width="14" height="14"/><circle cx="157" cy="40" r="7"/><path d="M182 40l7-7 7 7-7 7z"/><rect x="213" y="33" width="14" height="14"/><circle cx="247" cy="40" r="7"/><path d="M272 47l7-14 7 14z"/><path d="M303 40h14M310 33v14"/><circle cx="333" cy="40" r="7"/>
      <circle cx="10" cy="70" r="7"/><path d="M30 77l7-14 7 14z"/><rect x="63" y="63" width="14" height="14"/><circle cx="103" cy="70" r="7"/><path d="M123 70h14M130 63v14"/><rect x="150" y="63" width="14" height="14"/><circle cx="189" cy="70" r="7"/><path d="M213 77l7-14 7 14z"/><rect x="240" y="63" width="14" height="14"/><circle cx="279" cy="70" r="7"/><path d="M303 70l7-7 7 7-7 7z"/><rect x="326" y="63" width="14" height="14"/>
      <path d="M3 107l7-14 7 14z"/><circle cx="37" cy="100" r="7"/><rect x="63" y="93" width="14" height="14"/><path d="M96 100h14M103 93v14"/><circle cx="130" cy="100" r="7"/><path d="M150 107l7-14 7 14z"/><rect x="182" y="93" width="14" height="14"/><circle cx="220" cy="100" r="7"/><path d="M240 100l7-7 7 7-7 7z"/><circle cx="279" cy="100" r="7"/><rect x="303" y="93" width="14" height="14"/><circle cx="333" cy="100" r="7"/>
    </g>
  </svg>
  <div class="footer"><span class="brand"><i></i>qZephyra</span><span>Presentation Title Here</span></div>
</section>

<!-- 36 timeline continued -->
<section class="slide">
  <div class="abs" style="left:193px;top:0;width:1px;height:190px;background:var(--rule)"></div>
  <div class="abs tx" style="left:130px;top:30px;text-align:right"><b style="color:var(--ink)">Milestone</b><br>Short note here.</div>
  <div class="abs tx" style="left:200px;top:80px"><b style="color:var(--ink)">Milestone</b><br>Short note here.</div>
  <div class="abs tx" style="left:130px;top:130px;text-align:right"><b style="color:var(--ink)">Milestone</b><br>Short note here.</div>
  <div class="footer"><span class="brand"><i></i>qZephyra</span><span>Presentation Title Here</span></div>
</section>

<!-- 37 usa map -->
<section class="slide">
  <div class="title">USA Map</div>
  <div class="photo" style="left:14px;top:40px;width:180px;height:110px;background:linear-gradient(135deg,#d9e3ea,#5a3f8f 45%,#2b8a99 75%,#84b13c)" role="img" aria-label="Map of the United States with highlighted states"></div>
  <div class="abs" style="left:210px;top:44px;width:160px;font-size:9px;font-weight:600;color:var(--ink)">Your beautiful heading goes here</div>
  <p class="tx abs" style="left:210px;top:76px;width:160px">Replace this text with your own short words.</p>
  <svg class="abs" style="left:14px;top:156px" width="356" height="30" viewBox="0 0 356 30">
    <g fill="none" stroke-width="4" transform="rotate(-90)">
      <circle cx="-15" cy="20" r="10" stroke="var(--rule)"/><circle cx="-15" cy="20" r="10" stroke="var(--purple)" stroke-dasharray="40 63"/>
      <circle cx="-15" cy="110" r="10" stroke="var(--rule)"/><circle cx="-15" cy="110" r="10" stroke="var(--teal)" stroke-dasharray="25 63"/>
      <circle cx="-15" cy="200" r="10" stroke="var(--rule)"/><circle cx="-15" cy="200" r="10" stroke="var(--green)" stroke-dasharray="50 63"/>
      <circle cx="-15" cy="290" r="10" stroke="var(--rule)"/><circle cx="-15" cy="290" r="10" stroke="var(--blue)" stroke-dasharray="32 63"/>
    </g>
  </svg>
  <div class="footer"><span class="brand"><i></i>qZephyra</span><span>Presentation Title Here</span></div>
</section>

<!-- 38 data chart -->
<section class="slide">
  <div class="title">Data Chart</div>
  <div class="abs bg-navy" style="left:0;right:0;top:34px;height:80px"></div>
  <svg class="abs" style="left:0;top:44px" width="386" height="60" viewBox="0 0 386 60">
    <g fill="none" stroke-width="5" transform="rotate(-90)">
      <circle cx="-30" cy="60" r="24" stroke="#4a5a68"/><circle cx="-30" cy="60" r="24" stroke="var(--teal)" stroke-dasharray="75.4 151"/>
      <circle cx="-30" cy="148" r="24" stroke="#4a5a68"/><circle cx="-30" cy="148" r="24" stroke="var(--green)" stroke-dasharray="45.2 151"/>
      <circle cx="-30" cy="236" r="24" stroke="#4a5a68"/><circle cx="-30" cy="236" r="24" stroke="var(--blue)" stroke-dasharray="15.1 151"/>
      <circle cx="-30" cy="324" r="24" stroke="#4a5a68"/><circle cx="-30" cy="324" r="24" stroke="var(--purple)" stroke-dasharray="30.2 151"/>
    </g>
    <g fill="#fff" font-size="10" font-family="Montserrat, sans-serif" text-anchor="middle"><text x="60" y="34">50%</text><text x="148" y="34">30%</text><text x="236" y="34">10%</text><text x="324" y="34">20%</text></g>
  </svg>
  <div class="icon-label" style="left:30px;top:124px">Your Title Here<br><span style="font-weight:400;color:var(--muted)">Short note.</span></div>
  <div class="icon-label" style="left:118px;top:124px">Your Title Here<br><span style="font-weight:400;color:var(--muted)">Short note.</span></div>
  <div class="icon-label" style="left:206px;top:124px">Your Title Here<br><span style="font-weight:400;color:var(--muted)">Short note.</span></div>
  <div class="icon-label" style="left:294px;top:124px">Your Title Here<br><span style="font-weight:400;color:var(--muted)">Short note.</span></div>
  <div class="footer"><span class="brand"><i></i>qZephyra</span><span>Presentation Title Here</span></div>
</section>

<!-- 39 logo white -->
<section class="slide">
  <div class="abs" style="left:0;right:0;top:98px;text-align:center"><span class="brand big"><i></i>qZephyra</span></div>
</section>

<!-- 40 latest work -->
<section class="slide">
  <div class="title">Our Latest Work</div>
  <div class="photo ph-sky" style="left:14px;top:40px;width:82px;height:70px" role="img" aria-label="Project photograph one"></div>
  <div class="photo ph-city" style="left:104px;top:40px;width:82px;height:70px" role="img" aria-label="Project photograph two"></div>
  <div class="photo ph-grey" style="left:194px;top:40px;width:82px;height:70px" role="img" aria-label="Project photograph three"></div>
  <div class="photo ph-teal" style="left:284px;top:40px;width:86px;height:70px" role="img" aria-label="Project photograph four"></div>
  <p class="tx abs" style="left:14px;top:118px;width:82px"><b style="color:var(--ink)">Project Name</b><br>Short summary.</p>
  <p class="tx abs" style="left:104px;top:118px;width:82px"><b style="color:var(--ink)">Project Name</b><br>Short summary.</p>
  <p class="tx abs" style="left:194px;top:118px;width:82px"><b style="color:var(--ink)">Project Name</b><br>Short summary.</p>
  <p class="tx abs" style="left:284px;top:118px;width:82px"><b style="color:var(--ink)">Project Name</b><br>Short summary.</p>
  <div class="footer"><span class="brand"><i></i>qZephyra</span><span>Presentation Title Here</span></div>
</section>

<!-- 41 timeline hexagons -->
<section class="slide">
  <div class="title">Timeline</div>
  <svg class="abs" style="left:150px;top:30px" width="90" height="160" viewBox="0 0 90 160">
    <g fill="none" stroke="var(--teal-light)" stroke-width="1.5">
      <path d="M45 2l16 9v18l-16 9-16-9V11z"/><path d="M45 42l16 9v18l-16 9-16-9V51z"/><path d="M45 82l16 9v18l-16 9-16-9V91z"/><path d="M45 122l16 9v18l-16 9-16-9v-18z"/>
    </g>
    <g font-size="6" fill="var(--teal)" text-anchor="middle" font-family="Montserrat, sans-serif"><text x="45" y="22">2015</text><text x="45" y="62">2016</text><text x="45" y="102">2017</text><text x="45" y="142">2018</text></g>
  </svg>
  <p class="tx abs" style="left:250px;top:40px">Milestone note here.</p>
  <p class="tx abs" style="left:80px;top:80px">Milestone note here.</p>
  <p class="tx abs" style="left:250px;top:120px">Milestone note here.</p>
  <p class="tx abs" style="left:80px;top:160px">Milestone note here.</p>
</section>

<!-- 42 business process -->
<section class="slide">
  <div class="title">Business Process</div>
  <svg class="abs" style="left:133px;top:34px" width="120" height="150" viewBox="0 0 120 150">
    <path d="M60 15a60 60 0 0 1 58 55h-28a32 32 0 0 0-30-27z" fill="var(--teal)"/>
    <path d="M118 80a60 60 0 0 1-53 55v-28a32 32 0 0 0 25-27z" fill="var(--green)"/>
    <path d="M55 135a60 60 0 0 1-53-55h28a32 32 0 0 0 25 27z" fill="var(--purple)"/>
    <path d="M2 70a60 60 0 0 1 53-55v28a32 32 0 0 0-25 27z" fill="var(--blue)"/>
  </svg>
  <p class="tx abs" style="left:270px;top:50px"><b style="color:var(--ink)">Title Goes</b><br>Short note.</p>
  <p class="tx abs" style="left:270px;top:130px"><b style="color:var(--ink)">Title Goes</b><br>Short note.</p>
  <p class="tx abs" style="left:70px;top:50px"><b style="color:var(--ink)">Title Goes</b><br>Short note.</p>
  <p class="tx abs" style="left:70px;top:130px"><b style="color:var(--ink)">Title Goes</b><br>Short note.</p>
  <div class="footer"><span class="brand"><i></i>qZephyra</span><span>Presentation Title Here</span></div>
</section>

<!-- 43 timeline infographic -->
<section class="slide">
  <div class="title">Timeline Infographic</div>
  <svg class="abs" style="left:14px;top:60px" width="358" height="40" viewBox="0 0 358 40">
    <line x1="0" y1="20" x2="358" y2="20" stroke="var(--rule)" stroke-width="2"/>
    <rect x="10" y="8" width="50" height="24" fill="var(--teal)"/><rect x="80" y="8" width="50" height="24" fill="var(--green)"/><rect x="150" y="8" width="50" height="24" fill="var(--blue)"/><rect x="220" y="8" width="50" height="24" fill="var(--purple)"/><rect x="290" y="8" width="50" height="24" fill="var(--teal-dark)"/>
    <g fill="#fff" font-size="8" text-anchor="middle" font-family="Montserrat, sans-serif"><text x="35" y="23">2013</text><text x="105" y="23">2014</text><text x="175" y="23">2015</text><text x="245" y="23">2016</text><text x="315" y="23">2017</text></g>
  </svg>
  <p class="tx abs" style="left:24px;top:110px;width:60px">Milestone note.</p>
  <p class="tx abs" style="left:94px;top:110px;width:60px">Milestone note.</p>
  <p class="tx abs" style="left:164px;top:110px;width:60px">Milestone note.</p>
  <p class="tx abs" style="left:234px;top:110px;width:60px">Milestone note.</p>
  <p class="tx abs" style="left:304px;top:110px;width:60px">Milestone note.</p>
  <div class="footer"><span class="brand"><i></i>qZephyra</span><span>Presentation Title Here</span></div>
</section>

<!-- 44 timeline vertical -->
<section class="slide">
  <svg class="abs" style="left:150px;top:14px" width="90" height="190" viewBox="0 0 90 190">
    <line x1="45" y1="0" x2="45" y2="190" stroke="var(--rule)"/>
    <g fill="#fff" stroke="var(--teal-light)" stroke-width="1.5"><path d="M45 10l14 8v16l-14 8-14-8V18z"/><path d="M45 60l14 8v16l-14 8-14-8V68z"/><path d="M45 110l14 8v16l-14 8-14-8v-16z"/><path d="M45 150l14 8v16l-14 8-14-8v-16z"/></g>
  </svg>
  <p class="tx abs" style="left:250px;top:34px">Milestone note here.</p>
  <p class="tx abs" style="left:80px;top:84px">Milestone note here.</p>
  <p class="tx abs" style="left:250px;top:134px">Milestone note here.</p>
  <div class="footer"><span class="brand"><i></i>qZephyra</span><span>Presentation Title Here</span></div>
</section>

<!-- 45 timeline infographic 2 -->
<section class="slide">
  <div class="title">Timeline Infographic</div>
  <div class="abs" style="left:14px;right:14px;top:100px;height:2px;background:var(--teal-light)"></div>
  <div class="box" style="left:30px;top:50px;width:70px;height:40px;border-top:3px solid var(--green);background:#f4f6f7"><p class="tx">Milestone note.</p></div>
  <div class="box" style="left:115px;top:110px;width:70px;height:40px;border-top:3px solid var(--teal);background:#f4f6f7"><p class="tx">Milestone note.</p></div>
  <div class="box" style="left:200px;top:50px;width:70px;height:40px;border-top:3px solid var(--purple);background:#f4f6f7"><p class="tx">Milestone note.</p></div>
  <div class="box" style="left:285px;top:110px;width:70px;height:40px;border-top:3px solid var(--blue);background:#f4f6f7"><p class="tx">Milestone note.</p></div>
  <div class="footer"><span class="brand"><i></i>qZephyra</span><span>Presentation Title Here</span></div>
</section>

<!-- 46 table page -->
<section class="slide">
  <div class="title">Table Page</div>
  <table class="grid" style="left:14px;top:32px;width:358px">
    <tr><th style="background:var(--purple)">Column Heading</th><th style="background:var(--purple)">Column Heading</th><th style="background:var(--purple)">Column Heading</th></tr>
    <tr style="background:#efeaf6"><td>Table text here</td><td>Table text here</td><td>Table text here</td></tr>
    <tr><td>Table text here</td><td>Table text here</td><td>Table text here</td></tr>
    <tr style="background:#efeaf6"><td>Table text here</td><td>Table text here</td><td>Table text here</td></tr>
    <tr><td>Table text here</td><td>Table text here</td><td>Table text here</td></tr>
    <tr style="background:#efeaf6"><td>Table text here</td><td>Table text here</td><td>Table text here</td></tr>
    <tr><td>Table text here</td><td>Table text here</td><td>Table text here</td></tr>
    <tr style="background:#efeaf6"><td>Table text here</td><td>Table text here</td><td>Table text here</td></tr>
  </table>
  <div class="footer"><span class="brand"><i></i>qZephyra</span><span>Presentation Title Here</span></div>
</section>

<!-- 47 fishbone chevrons -->
<section class="slide">
  <div class="title">Fishbone Diagram</div>
  <svg class="abs" style="left:14px;top:60px" width="358" height="80" viewBox="0 0 358 80">
    <path d="M0 20h60l20 20-20 20H0l20-20z" fill="var(--teal)"/>
    <path d="M70 20h60l20 20-20 20H70l20-20z" fill="var(--blue)"/>
    <path d="M140 20h60l20 20-20 20h-60l20-20z" fill="var(--purple)"/>
    <path d="M210 20h60l20 20-20 20h-60l20-20z" fill="var(--green)"/>
    <circle cx="325" cy="40" r="22" fill="var(--teal-dark)"/>
    <text x="325" y="43" fill="#fff" font-size="7" text-anchor="middle" font-family="Montserrat, sans-serif">Result</text>
  </svg>
  <p class="tx abs" style="left:24px;top:40px">Cause one</p><p class="tx abs" style="left:94px;top:146px">Cause two</p><p class="tx abs" style="left:164px;top:40px">Cause three</p><p class="tx abs" style="left:234px;top:146px">Cause four</p>
  <div class="footer"><span class="brand"><i></i>qZephyra</span><span>Presentation Title Here</span></div>
</section>

<!-- 48 fishbone arrows -->
<section class="slide">
  <div class="title">Fishbone Diagram</div>
  <svg class="abs" style="left:14px;top:40px" width="358" height="130" viewBox="0 0 358 130">
    <line x1="0" y1="65" x2="310" y2="65" stroke="var(--teal-light)" stroke-width="3"/>
    <path d="M310 55l14 10-14 10z" fill="var(--teal-light)"/>
    <g stroke="var(--teal-light)" stroke-width="2" fill="none"><path d="M40 20l30 45M100 20l30 45M160 20l30 45M220 20l30 45M40 110l30-45M100 110l30-45M160 110l30-45M220 110l30-45"/></g>
    <text x="335" y="68" font-size="7" fill="var(--teal)" font-family="Montserrat, sans-serif">Result</text>
  </svg>
  <div class="footer"><span class="brand"><i></i>qZephyra</span><span>Presentation Title Here</span></div>
</section>

<!-- 49 fishbone fish -->
<section class="slide">
  <div class="title">Fishbone Diagram</div>
  <svg class="abs" style="left:14px;top:40px" width="358" height="130" viewBox="0 0 358 130">
    <path d="M0 40l20 25-20 25z" fill="var(--teal)"/>
    <line x1="20" y1="65" x2="300" y2="65" stroke="var(--teal)" stroke-width="2"/>
    <g fill="none" stroke="var(--teal-light)" stroke-width="1.5"><path d="M60 65q15-30 40-40M130 65q15-30 40-40M200 65q15-30 40-40M60 65q15 30 40 40M130 65q15 30 40 40M200 65q15 30 40 40"/></g>
    <path d="M300 45q40 0 55 20-15 20-55 20z" fill="var(--teal)"/>
    <g font-size="5" fill="var(--muted)" font-family="Montserrat, sans-serif"><text x="100" y="22">Cause</text><text x="170" y="22">Cause</text><text x="240" y="22">Cause</text><text x="100" y="114">Cause</text><text x="170" y="114">Cause</text><text x="240" y="114">Cause</text></g>
  </svg>
  <div class="footer"><span class="brand"><i></i>qZephyra</span><span>Presentation Title Here</span></div>
</section>

<!-- 50 fishbone lines -->
<section class="slide">
  <div class="title">Fishbone Diagram</div>
  <svg class="abs" style="left:14px;top:36px" width="358" height="140" viewBox="0 0 358 140">
    <line x1="0" y1="70" x2="340" y2="70" stroke="var(--teal)" stroke-width="2"/>
    <g stroke="var(--teal-light)" stroke-width="1.5"><path d="M50 15l40 55M130 15l40 55M210 15l40 55M50 125l40-55M130 125l40-55M210 125l40-55"/></g>
    <g stroke="var(--rule)"><path d="M60 30h25M70 45h25M140 30h25M150 45h25M220 30h25M230 45h25M60 110h25M70 95h25M140 110h25M150 95h25M220 110h25M230 95h25"/></g>
    <rect x="300" y="58" width="58" height="24" fill="var(--teal)"/>
    <text x="329" y="73" fill="#fff" font-size="7" text-anchor="middle" font-family="Montserrat, sans-serif">Result</text>
  </svg>
  <div class="footer"><span class="brand"><i></i>qZephyra</span><span>Presentation Title Here</span></div>
</section>

<!-- 51 funnel infographic -->
<section class="slide">
  <div class="title">Funnel Infographic</div>
  <svg class="abs" style="left:200px;top:34px" width="150" height="150" viewBox="0 0 150 150">
    <path d="M0 0h150l-15 35H15z" fill="var(--teal)"/>
    <path d="M18 40h114l-15 35H33z" fill="var(--blue)"/>
    <path d="M36 80h78l-15 35H51z" fill="var(--green-dark)"/>
    <path d="M54 120h42l-10 28H64z" fill="var(--green)"/>
  </svg>
  <div class="abs" style="left:40px;top:40px">
    <p class="tx" style="margin-bottom:14px"><b style="color:var(--ink)">Your Title Here</b><br>Short stage note.</p>
    <p class="tx" style="margin-bottom:14px"><b style="color:var(--ink)">Your Title Here</b><br>Short stage note.</p>
    <p class="tx" style="margin-bottom:14px"><b style="color:var(--ink)">Your Title Here</b><br>Short stage note.</p>
    <p class="tx"><b style="color:var(--ink)">Your Title Here</b><br>Short stage note.</p>
  </div>
  <div class="footer"><span class="brand"><i></i>qZephyra</span><span>Presentation Title Here</span></div>
</section>

<!-- 52 cylinder funnel -->
<section class="slide">
  <div class="title">Cylinder Funnel</div>
  <svg class="abs" style="left:30px;top:36px" width="160" height="150" viewBox="0 0 160 150">
    <path d="M0 10h160l-20 40H20z" fill="var(--teal)"/><ellipse cx="80" cy="10" rx="80" ry="9" fill="var(--teal-light)"/>
    <path d="M20 50h120l-20 40H40z" fill="var(--blue)"/>
    <path d="M40 90h80l-20 40H60z" fill="var(--green)"/>
    <rect x="60" y="130" width="40" height="18" fill="var(--green-dark)"/>
  </svg>
  <div class="abs" style="left:220px;top:50px">
    <p class="tx" style="margin-bottom:12px"><b style="color:var(--ink)">Products A</b><br>Short stage note.</p>
    <p class="tx" style="margin-bottom:12px"><b style="color:var(--ink)">Products B</b><br>Short stage note.</p>
    <p class="tx"><b style="color:var(--ink)">Products C</b><br>Short stage note.</p>
  </div>
  <div class="footer"><span class="brand"><i></i>qZephyra</span><span>Presentation Title Here</span></div>
</section>

<!-- 53 cylinder funnel stacked -->
<section class="slide">
  <div class="title">Cylinder Funnel</div>
  <svg class="abs" style="left:133px;top:30px" width="120" height="160" viewBox="0 0 120 160">
    <ellipse cx="60" cy="12" rx="60" ry="10" fill="var(--teal-light)"/>
    <path d="M0 12h120v22c0 6-27 10-60 10S0 40 0 34z" fill="var(--teal)"/>
    <path d="M12 50h96v22c0 6-21 10-48 10s-48-4-48-10z" fill="var(--blue)"/>
    <path d="M26 88h68v22c0 6-15 10-34 10s-34-4-34-10z" fill="var(--green)"/>
    <path d="M40 126h40v22c0 5-9 8-20 8s-20-3-20-8z" fill="var(--green-dark)"/>
  </svg>
  <p class="tx abs" style="left:40px;top:50px">Your Title Here</p>
  <p class="tx abs" style="left:270px;top:88px">Your Title Here</p>
  <p class="tx abs" style="left:40px;top:126px">Your Title Here</p>
  <p class="tx abs" style="left:270px;top:164px">Your Title Here</p>
  <div class="footer"><span class="brand"><i></i>qZephyra</span><span>Presentation Title Here</span></div>
</section>

<!-- 54 dashboard analysis -->
<section class="slide">
  <div class="title">Dashboard Analysis</div>
  <table class="grid" style="left:14px;top:32px;width:358px">
    <tr><th style="background:var(--ink)">Metric</th><th style="background:var(--ink)">Status</th><th style="background:var(--ink)">Q1</th><th style="background:var(--ink)">Q2</th></tr>
    <tr><td>Metric name</td><td><svg width="8" height="8"><circle cx="4" cy="4" r="4" fill="var(--green)"/></svg></td><td><svg width="8" height="8"><circle cx="4" cy="4" r="4" fill="var(--teal)"/></svg></td><td><svg width="8" height="8"><circle cx="4" cy="4" r="4" fill="var(--purple)"/></svg></td></tr>
    <tr><td>Metric name</td><td><svg width="8" height="8"><circle cx="4" cy="4" r="4" fill="var(--teal)"/></svg></td><td><svg width="8" height="8"><circle cx="4" cy="4" r="4" fill="var(--green)"/></svg></td><td><svg width="8" height="8"><circle cx="4" cy="4" r="4" fill="var(--teal)"/></svg></td></tr>
    <tr><td>Metric name</td><td><svg width="8" height="8"><circle cx="4" cy="4" r="4" fill="var(--purple)"/></svg></td><td><svg width="8" height="8"><circle cx="4" cy="4" r="4" fill="var(--teal)"/></svg></td><td><svg width="8" height="8"><circle cx="4" cy="4" r="4" fill="var(--green)"/></svg></td></tr>
    <tr><td>Metric name</td><td><svg width="8" height="8"><circle cx="4" cy="4" r="4" fill="var(--green)"/></svg></td><td><svg width="8" height="8"><circle cx="4" cy="4" r="4" fill="var(--purple)"/></svg></td><td><svg width="8" height="8"><circle cx="4" cy="4" r="4" fill="var(--teal)"/></svg></td></tr>
    <tr><td>Metric name</td><td><svg width="8" height="8"><circle cx="4" cy="4" r="4" fill="var(--teal)"/></svg></td><td><svg width="8" height="8"><circle cx="4" cy="4" r="4" fill="var(--green)"/></svg></td><td><svg width="8" height="8"><circle cx="4" cy="4" r="4" fill="var(--green)"/></svg></td></tr>
  </table>
  <div class="footer"><span class="brand"><i></i>qZephyra</span><span>Presentation Title Here</span></div>
</section>

<!-- 55 table -->
<section class="slide">
  <div class="title">Table</div>
  <table class="grid" style="left:14px;top:32px;width:358px">
    <tr><th style="background:var(--teal)">Item</th><th style="background:var(--teal)">Column</th><th style="background:var(--teal)">Column</th><th style="background:var(--teal)">Column</th><th style="background:var(--teal)">Column</th></tr>
    <tr><td>Row text</td><td>Value</td><td>Value</td><td>Value</td><td>Value</td></tr>
    <tr><td>Row text</td><td>Value</td><td>Value</td><td>Value</td><td>Value</td></tr>
    <tr><td>Row text</td><td>Value</td><td>Value</td><td>Value</td><td>Value</td></tr>
    <tr><td>Row text</td><td>Value</td><td>Value</td><td>Value</td><td>Value</td></tr>
    <tr><td>Row text</td><td>Value</td><td>Value</td><td>Value</td><td>Value</td></tr>
    <tr><td>Row text</td><td>Value</td><td>Value</td><td>Value</td><td>Value</td></tr>
  </table>
  <div class="footer"><span class="brand"><i></i>qZephyra</span><span>Presentation Title Here</span></div>
</section>

<!-- 56 dashboard cards -->
<section class="slide">
  <div class="title">Dashboard Analysis</div>
  <div class="box" style="left:14px;top:34px;width:112px;height:64px;border:1px solid var(--rule)"><p class="tx">Metric title</p><div class="abs bg-teal" style="left:0;right:0;bottom:0;height:14px;font-size:5px;color:#fff;padding:4px 8px">Label Here</div></div>
  <div class="box" style="left:137px;top:34px;width:112px;height:64px;border:1px solid var(--rule)"><p class="tx">Metric title</p><div class="abs bg-teal" style="left:0;right:0;bottom:0;height:14px;font-size:5px;color:#fff;padding:4px 8px">Label Here</div></div>
  <div class="box" style="left:260px;top:34px;width:112px;height:64px;border:1px solid var(--rule)"><p class="tx">Metric title</p><div class="abs bg-teal" style="left:0;right:0;bottom:0;height:14px;font-size:5px;color:#fff;padding:4px 8px">Label Here</div></div>
  <div class="box" style="left:14px;top:108px;width:112px;height:64px;border:1px solid var(--rule)"><p class="tx">Metric title</p><div class="abs bg-teal" style="left:0;right:0;bottom:0;height:14px;font-size:5px;color:#fff;padding:4px 8px">Label Here</div></div>
  <div class="box" style="left:137px;top:108px;width:112px;height:64px;border:1px solid var(--rule)"><p class="tx">Metric title</p><div class="abs bg-teal" style="left:0;right:0;bottom:0;height:14px;font-size:5px;color:#fff;padding:4px 8px">Label Here</div></div>
  <div class="box" style="left:260px;top:108px;width:112px;height:64px;border:1px solid var(--rule)"><p class="tx">Metric title</p><div class="abs bg-teal" style="left:0;right:0;bottom:0;height:14px;font-size:5px;color:#fff;padding:4px 8px">Label Here</div></div>
  <div class="footer"><span class="brand"><i></i>qZephyra</span><span>Presentation Title Here</span></div>
</section>

<!-- 57 thank you -->
<section class="slide">
  <div class="photo" style="inset:0;background:linear-gradient(135deg,#8dbb46,#2b8a99 55%,#17505c)" role="img" aria-label="Digital technology background photograph"></div>
  <div class="abs big-title" style="left:30px;top:92px;font-size:18px">Thank You</div>
  <div class="abs" style="left:230px;top:80px;font-size:5.5px;line-height:1.9;color:#e6f3f4">
    <span class="brand light" style="font-size:8px"><i></i>qZephyra</span><br>
    +1 408 555 0142<br>
    hello@qzephyra.example<br>
    www.qzephyra.example
  </div>
</section>

</main>
</body>
</html>
```